" A Construtora BAVO nasceu para tornar o setor da construçao civil mais industrializado e SUSTENTAVEL!!! Trouxe ao Brasil o sistema construtivo que é utilizado nos Estados Unidos e Europa. Com soluçoes inovadoras para a construçao de casas, aliando tecnologia e eficiência em produtos e serviços, Nosso foco de trabalho é a construçao de residências e imóveis comerciais em Steel Frame. A estrutura da casa inteira é feita usando aço leve galvanizado e perfis metálicos revestidos na area externa com placa cimenticia e internamente com placa de drywall "

```html
<!DOCTYPE html>
<html lang="pt-BR">
<head>
<meta charset="UTF-8">
<title>Construtora BAVO – Banner</title>
<link href="https://fonts.googleapis.com/css2?family=Open+Sans:wght@400;700;800&display=swap" rel="stylesheet">
<style>
  :root {
    --backdrop: #e9e6e2;
    --panel-light-a: #ffffff;
    --panel-light-b: #dcdfe2;
    --brand-blue: #1e5e80;
    --brand-blue-dark: #17486a;
    --ink-blue: #1b3f63;
    --brand-green: #76b82a;
    --ink-grey: #4a4f55;
  }
  * { margin: 0; padding: 0; box-sizing: border-box; }
  html, body {
    width: 1200px;
    height: 1200px;
    overflow: hidden;
    background: var(--backdrop);
    font-family: "Open Sans", Arial, sans-serif;
  }
  .canvas {
    position: relative;
    width: 1200px;
    height: 1200px;
  }
  .banner {
    position: absolute;
    left: 197px;
    top: 427px;
    width: 850px;
    height: 312px;
    background: linear-gradient(120deg, var(--panel-light-a) 0%, var(--panel-light-b) 100%);
    box-shadow: 0 10px 24px rgba(0, 0, 0, 0.25);
    overflow: hidden;
  }
  .banner__blue-panel {
    position: absolute;
    left: 408px;
    top: 0;
    width: 442px;
    height: 312px;
    background: var(--brand-blue);
  }
  .tile {
    position: absolute;
    background: var(--brand-blue-dark);
    box-shadow: 2px 3px 6px rgba(0, 0, 0, 0.3);
  }
  .tile--a { left: 379px; top: 120px; width: 74px; height: 72px; background: var(--brand-blue); }
  .tile--b { left: 240px; top: 247px; width: 50px; height: 48px; }
  .tile--c { left: 350px; top: 257px; width: 52px; height: 48px; }

  .brand {
    position: absolute;
    left: 34px;
    top: 48px;
    display: flex;
    align-items: center;
    gap: 12px;
  }
  .brand__square {
    width: 38px;
    height: 38px;
    background: var(--brand-green);
  }
  .brand__name {
    font-weight: 800;
    font-size: 30px;
    line-height: 1;
    color: var(--ink-grey);
    white-space: nowrap;
  }
  .tagline {
    position: absolute;
    left: 24px;
    top: 140px;
    font-weight: 700;
    font-size: 18px;
    line-height: 1.3;
    color: var(--ink-blue);
    white-space: nowrap;
  }
  .emblem {
    position: absolute;
    left: 543px;
    top: 108px;
    width: 260px;
    text-align center;
    text-align: center;
    font-weight: 800;
    font-size: 80px;
    line-height: 1;
    color: var(--brand-green);
  }
</style>
</head>
<body>
  <div class="canvas">
    <section class="banner">
      <div class="banner__blue-panel"></div>

      <div class="brand">
        <span class="brand__square"></span>
        <span class="brand__name">Construtora BAVO</span>
      </div>

      <p class="tagline">A Construção Civil<br>mais Industrializada e Sustentável!</p>

      <span class="tile tile--a"></span>
      <span class="tile tile--b"></span>
      <span class="tile tile--c"></span>

      <div class="emblem">BAVO</div>
    </section>
  </div>
</body>
</html>
```